Timeline flyer

Hi, we are an agency, our business is to orienteates student to study abroad in Germany. For that, we enroll them in language schools in Germany and help them to find an accomodation.
Students are always lost we thinked about a timeline to help them figure out what they have to do once in Germany so they don't miss delays.
You can find in the attachement an example that i made in powerpoint but it's really basic and it's only for u so you can understant what the timeline should look like.
We need two time lines.
For the first one (file first timeline)
Title : Procédure pour intégrer le semestre d’hiver dans les universités Allemandes
The first paragraph (up on the left in my proposition) : L’étudiant devra pendant ces mois débuter ses cours d’allemand en Tunisie et les poursuivre en Allemagne après l’obtention du Visa d’étude. L’atteinte du niveau C1 est primordiale pour la bonne réussite du test Kel ou le MRT.
The second paragraph (below on the left in my proposition) : L’étudiant devra à cette date avoir déjà passer le test KEL ou le MRT pour pouvoir être à temps pour les inscriptions universitaires. Il faut compter 6 semaines pour le test Kel et 2 à 3 semaines pour obtenir les résultats des tests.
The third one (up on the right in my proposition) : Le dernier délais d’inscription pour pouvoir intégrer une université Allemande pendant la rentrée hivernale (15 Octobre).
The last one (below on the right in my proposition) : Rentrée universitaire
For the second one (file second timeline) :
Title : Procédure pour intégrer le semestre d’été dans les universités Allemandes *
The third one (up on the right in my proposition) : Le dernier délais d’inscription pour pouvoir intégrer une université Allemande pendant la rentrée estivale (15 Avril).
There is also an additional sentence below in the right for this one : * Les spécialités assurées pendant les semestres d’été sont limitées.
You can also find in the attachement our flyers (so you can inspire youself with the color and the design), we want our student to recognize that the flyer is related to our agency so please try to use colors that are matched with the other flyer.
Also, you can find our Logo in the attachement.
Thank you :)
Waiting for your propositions ! :)

```html
<!DOCTYPE html>
<html lang="fr">
<head>
<meta charset="utf-8">
<title>Timeline flyer – Wegweiser Centre</title>
<link rel="stylesheet" href="https://fonts.googleapis.com/css2?family=Open+Sans:wght@400;600;700&display=swap">
<style>
:root{
  --page-bg:#b4b4b8;
  --blue-light:#1e9be0;
  --blue-mid:#1478c4;
  --blue-deep:#0c5ea6;
  --lime:#c8d400;
  --green-a:#7cbf80;
  --green-b:#5fa86a;
  --white:#ffffff;
  --ink-on-lime:#ffffff;
}
*{box-sizing:border-box;margin:0;padding:0}
html,body{width:1200px;height:900px;overflow:hidden;background:var(--page-bg);font-family:"Open Sans",Arial,sans-serif;color:var(--white)}
.flyer{position:absolute;left:300px;top:15px;width:600px;height:870px;overflow:hidden;
  background:linear-gradient(170deg,var(--blue-light) 0%,var(--blue-mid) 55%,var(--blue-deep) 100%)}
.city-backdrop{position:absolute;left:0;right:0;top:280px;height:520px;
  background:linear-gradient(180deg,rgba(255,255,255,0) 0%,rgba(10,70,130,.35) 40%,rgba(8,60,115,.45) 75%,rgba(255,255,255,0) 100%)}
.brand{position:absolute;top:46px;right:44px;display:flex;align-items:center;gap:10px}
.brand-dot{width:16px;height:16px;border-radius:50%;background:var(--lime)}
.brand-name{font-size:19px;font-weight:700;color:var(--lime);line-height:1}
.section-title{position:absolute;font-size:19px;font-weight:600;text-transform:uppercase;line-height:1.2;letter-spacing:.3px}
.title-winter{left:60px;top:110px}
.title-summer{right:40px;top:505px;text-align:right}
.rule{position:absolute;height:1px;background:var(--white)}
.note{position:absolute;border:1px dashed var(--white);padding:5px 7px;font-size:9.5px;line-height:1.3;text-align:justify}
.note.small{text-align:center;padding:3px 8px}
.bracket{position:absolute;height:10px;border:1px solid var(--white);border-bottom:none}
.tick{position:absolute;width:1px;background:var(--white)}
.timeline{position:absolute;left:24px;display:flex;align-items:center;height:100px}
.timeline-tab{width:22px;height:34px;background:var(--lime)}
.month{width:28px;height:100px;display:flex;align-items:center;justify-content:center;font-size:9px;font-weight:600}
.month:nth-child(odd){background:var(--green-a)}
.month:nth-child(even){background:var(--green-b)}
.month span{writing-mode:vertical-rl;transform:rotate(180deg);white-space:nowrap}
.month.key{width:52px;background:var(--lime);color:var(--ink-on-lime);text-align:center;line-height:1.15;font-size:9.5px}
.month.key span{writing-mode:horizontal-tb;transform:none}
.timeline-arrow{width:40px;height:60px}
</style>
</head>
<body>
<main class="flyer">
  <div class="city-backdrop" role="img" aria-label="Vue de ville allemande en fond, teintée de bleu"></div>

  <div class="brand"><span class="brand-dot"></span><span class="brand-name">Wegweiser Centre</span></div>

  <!-- Semestre d'hiver -->
  <h2 class="section-title title-winter">Procédure pour intégrer<br>le semestre d’hiver dans<br>les universités Allemandes</h2>
  <div class="rule" style="left:30px;top:195px;width:330px"></div>

  <p class="note" style="left:50px;top:210px;width:300px">L’étudiant devra pendant ces mois débuter ses cours d’allemand en Tunisie et les poursuivre en Allemagne après l’obtention du Visa d’étude. L’atteinte du niveau C1 est primordiale pour la bonne réussite du test Kel ou le MRT.</p>
  <p class="note" style="left:372px;top:210px;width:190px">Le dernier délais d’inscription pour pouvoir intégrer une université Allemande pendant la rentrée hivernale (15 Octobre).</p>

  <div class="tick" style="left:200px;top:284px;height:14px"></div>
  <div class="bracket" style="left:46px;top:298px;width:310px"></div>
  <div class="tick" style="left:460px;top:270px;height:40px"></div>

  <div class="timeline" style="top:310px">
    <div class="timeline-tab"></div>
    <div class="month"><span>SEP 2016</span></div>
    <div class="month"><span>OCT 2016</span></div>
    <div class="month"><span>NOV 2016</span></div>
    <div class="month"><span>DÉC 2016</span></div>
    <div class="month"><span>JAN 2017</span></div>
    <div class="month"><span>FEV 2017</span></div>
    <div class="month"><span>MARS 2017</span></div>
    <div class="month"><span>AVR 2017</span></div>
    <div class="month key"><span>DÉBUT<br>MAI<br>2017</span></div>
    <div class="month"><span>JUI 2017</span></div>
    <div class="month key"><span>15<br>JUILLET<br>2017</span></div>
    <div class="month"><span>AOÛT 2017</span></div>
    <div class="month"><span>SEP 2017</span></div>
    <div class="month key"><span>15<br>OCTOBRE<br>2017</span></div>
    <div class="month"><span>NOV 2017</span></div>
    <svg class="timeline-arrow" viewBox="0 0 40 60" aria-hidden="true"><polygon points="0,15 18,15 18,0 40,30 18,60 18,45 0,45" fill="var(--lime)"/></svg>
  </div>

  <div class="tick" style="left:368px;top:410px;height:22px"></div>
  <p class="note" style="left:120px;top:432px;width:300px">L’étudiant devra à cette date avoir déjà passer le test KEL ou le MRT pour pouvoir être à temps pour les inscriptions universitaires. Il faut compter 6 semaines pour le test Kel et 2 à 3 semaines pour obtenir les résultats des tests.</p>
  <div class="tick" style="left:486px;top:410px;height:12px"></div>
  <p class="note small" style="left:430px;top:422px">Rentrée universitaire.</p>

  <!-- Semestre d'été -->
  <h2 class="section-title title-summer">Procédure pour intégrer<br>le semestre d’été dans<br>les universités Allemandes</h2>
  <div class="rule" style="left:230px;top:585px;width:350px"></div>

  <p class="note" style="left:60px;top:600px;width:300px">L’étudiant devra pendant ces mois débuter ses cours d’allemand en Tunisie et les poursuivre en Allemagne après l’obtention du Visa d’étude. L’atteinte du niveau C1 est primordiale pour la bonne réussite du test Kel ou le MRT.</p>
  <p class="note" style="left:380px;top:600px;width:185px">Le dernier délais d’inscription pour pouvoir intégrer une université Allemande pendant la rentrée estivale (15 Avril).</p>

  <div class="tick" style="left:210px;top:674px;height:4px"></div>
  <div class="bracket" style="left:46px;top:678px;width:310px"></div>
  <div class="tick" style="left:486px;top:660px;height:30px"></div>

  <div class="timeline" style="top:690px">
    <div class="timeline-tab"></div>
    <div class="month"><span>MARS 2017</span></div>
    <div class="month"><span>AVR 2017</span></div>
    <div class="month"><span>MAI 2017</span></div>
    <div class="month"><span>JUIN 2017</span></div>
    <div class="month"><span>JUI 2017</span></div>
    <div class="month"><span>AOÛT 2017</span></div>
    <div class="month"><span>SEP 2017</span></div>
    <div class="month"><span>OCT 2017</span></div>
    <div class="month key"><span>DÉBUT<br>NOV<br>2017</span></div>
    <div class="month"><span>DÉC 2017</span></div>
    <div class="month key"><span>15<br>JAN<br>2018</span></div>
    <div class="month"><span>FEV 2018</span></div>
    <div class="month"><span>MARS 2018</span></div>
    <div class="month key"><span>15<br>AVRIL<br>2018</span></div>
    <div class="month"><span>MAI 2018</span></div>
    <svg class="timeline-arrow" viewBox="0 0 40 60" aria-hidden="true"><polygon points="0,15 18,15 18,0 40,30 18,60 18,45 0,45" fill="var(--lime)"/></svg>
  </div>

  <div class="tick" style="left:368px;top:790px;height:14px"></div>
  <p class="note" style="left:120px;top:804px;width:300px">L’étudiant devra à cette date avoir déjà passer le test KEL ou le MRT pour pouvoir être à temps pour les inscriptions universitaires. Il faut compter 6 semaines pour le test Kel et 2 à 3 semaines pour obtenir les résultats des tests.</p>
  <div class="tick" style="left:486px;top:790px;height:8px"></div>
  <p class="note small" style="left:432px;top:798px">Rentrée universitaire.</p>
  <p class="note small" style="left:430px;top:826px;width:150px">* Les spécialités assurées pendant les semestres d’été sont limitées.</p>
</main>
</body>
</html>
```